Developer needs a Software blog Design

I need a design for my software blog (I'm a developer). The design should include a homepage for browser and for mobile.

Following is a wireframe: https://sketchgrid.io/kTmwqe.

The sidebar can also include my picture I you think it should.

In the mobile version the about me and subscribe with email should be popup or dropdown.

I'm currently using this: http://valpirek.quillhost.io/ which I like, but doesn't have all the component I want on the sidebar and I want something unique.

The most importnant is simple, clean and responsive.

Designs that I like:
http://blog.tarvuso.com/
http://xwrp.net/layoutbazaar/?theme=fels
http://demo.layoutvireo.com/#singularly

Out come should be a psd file with homepage and mobile homepage (and dropdowns variation for the mobile).

Target Market(s)

developers

Industry/Entity Type

Software

Font styles to use
Sans Serif

Requirements
Must have
• clean and simple. responsive. main post area need to be wide enough.

```html
<!DOCTYPE html>
<html lang="en">
<head>
<meta charset="utf-8">
<title>Token-Based PubSub — Valpirek</title>
<link href="https://fonts.googleapis.com/css2?family=Bree+Serif&family=Lato:ital,wght@0,400;0,700;1,700&display=swap" rel="stylesheet">
<style>
:root{
  --side-dark:#1f3042;
  --side-mid:#2d4660;
  --side-text:#e8eef4;
  --side-muted:#b9c6d3;
  --accent-green:#a8d5b0;
  --green-soft:#cfe6c9;
  --ink:#5a5a5a;
  --ink-dark:#3c4650;
  --link-blue:#1f3a56;
  --line:#d6d6d6;
  --btn-grey:#666;
  --chirp:#2ea4e6;
  --feed:#e4552a;
  --white:#fff;
}
*{box-sizing:border-box;margin:0;padding:0}
html,body{width:1200px;height:1094px;overflow:hidden;background:var(--white)}
body{position:relative;font-family:"Lato",sans-serif;color:var(--ink)}
.sidebar{position:absolute;left:0;top:0;width:382px;height:1094px;
  background:linear-gradient(90deg,var(--side-mid) 0%,#2a425b 70%,var(--side-dark) 100%);color:var(--side-text)}
.abs{position:absolute}
.avatar{left:127px;top:38px;width:169px;height:169px;border-radius:50%;border:5px solid #fff;
  background:radial-gradient(circle at 50% 40%,#b9b3ad 0%,#8d8b88 45%,#3a3d44 100%)}
.owner-name{left:0;width:422px;top:224px;text-align:center;font-family:"Bree Serif",serif;font-size:25px;letter-spacing:1px;color:#c9d5e2}
.bio{left:67px;top:268px;width:294px;font-size:13.5px;line-height:20px;letter-spacing:.6px}
.socials{left:110px;top:358px;display:flex;gap:14px}
.socials span{width:17px;height:17px;border-radius:50%;background:#fff;display:block}
.search{left:67px;top:405px;width:291px;height:37px;border-radius:3px;
  background:linear-gradient(90deg,#dcecd3,#a9d2ae);display:flex;align-items:center;justify-content:space-between;padding:0 12px}
.search em{font-weight:700;font-size:13px;color:var(--ink-dark);letter-spacing:.5px}
.side-head{left:66px;width:292px;font-family:"Bree Serif",serif;font-size:19px;letter-spacing:.5px;color:#fff;border-bottom:1px solid #c5ced8;padding-bottom:3px}
.rpost{left:69px;width:289px;font-size:13px}
.rpost h4{font-size:13.5px;font-weight:700;margin-bottom:7px}
.rpost p{line-height:16px;letter-spacing:.4px;width:270px}
.rpost .foot{display:flex;justify-content:space-between;margin-top:5px;color:var(--side-muted);padding-right:18px}
.rpost .more{color:var(--green-soft);font-weight:700}
.rpost .more::before{content:"▸ ";font-size:9px}
.rdiv{left:67px;width:291px;top:608px;border-top:1px solid #3e5670}
.email{left:67px;top:777px;width:291px;height:34px;background:#9aafc3;border-radius:2px;color:#fff;font-size:13.5px;display:flex;align-items:center;justify-content:space-between;padding:0 13px}
.cta{left:66px;width:292px;height:47px;border-radius:4px;display:flex;align-items:center;color:#fff;font-family:"Bree Serif",serif;font-size:22px;letter-spacing:.5px}
.cta .ico{width:55px;height:25px;border-right:1px solid rgba(255,255,255,.5);display:flex;align-items:center;justify-content:center}
.cta .ico i{width:16px;height:16px;background:#fff;display:block;border-radius:2px}
.cta .label{flex:1;text-align:center}
.cta.chirp{top:830px;background:linear-gradient(#53bdf1,var(--chirp));border-bottom:2px solid #1d82bd}
.cta.feed{top:889px;background:linear-gradient(#f2794d,var(--feed));border-bottom:2px solid #b63e18}
.copy{left:0;width:422px;top:954px;text-align:center;font-size:13.5px}

.post-title{left:401px;width:768px;top:16px;text-align:center;font-family:"Bree Serif",serif;font-size:32px;color:#666}
.meta{left:401px;width:768px;top:64px;display:flex;justify-content:center;gap:12px;align-items:center;font-family:"Bree Serif",serif;font-size:16px;color:#666}
.meta b{color:#222;font-weight:400}
.excerpt{left:401px;width:747px;top:116px;font-size:13.5px;line-height:24px;color:#666}
.share{left:404px;top:240px;display:flex;align-items:center;gap:7px;font-family:"Bree Serif",serif;font-size:13px;color:#555}
.share .dot{width:27px;height:27px;border-radius:50%;background:var(--link-blue);display:block}
.share .lbl{margin-right:8px}
.read{left:1027px;top:235px;width:121px;height:37px;background:var(--btn-grey);border-bottom:2px solid #444;border-radius:3px;color:#fff;font-family:"Bree Serif",serif;font-size:15px;display:flex;align-items:center;justify-content:center;letter-spacing:.5px}
.c-head{left:404px;top:290px;width:744px;font-family:"Bree Serif",serif;font-size:25px;color:#666;border-bottom:1px solid #ccc;padding-bottom:6px}
.c-head::after{content:"";position:absolute;left:1px;bottom:-3px;width:163px;height:5px;background:var(--accent-green)}
.c-ava{width:75px;height:75px;border-radius:6px;border:3px solid #fff;box-shadow:0 0 0 1px #ccc,0 1px 3px rgba(0,0,0,.3)}
.ava-a{background:linear-gradient(160deg,#7e8a72,#3b3a35)}
.ava-b{background:linear-gradient(160deg,#e6e7ea,#7d6a5c)}
.ava-c{background:linear-gradient(160deg,#b6b6b6,#4f6e9a 60%,#8a8a8a)}
.ava-d{background:linear-gradient(160deg,#e0e6ee,#9db2cc)}
.c-box{height:75px;border:1px solid #ddd;border-radius:6px;padding:10px 16px 0 14px;font-size:13.5px;color:#666}
.c-box .top{display:flex;justify-content:space-between;color:var(--link-blue);margin-bottom:6px}
.c-box p{line-height:17px}
.see-all{left:1076px;top:935px;width:72px;height:24px;background:var(--accent-green);color:#fff;font-size:13px;display:flex;align-items:center;justify-content:center;border-radius:2px}
</style>
</head>
<body>
<aside class="sidebar">
  <div class="abs avatar" role="img" aria-label="Portrait photo of the blog author"></div>
  <h1 class="abs owner-name">VALPIREK</h1>
  <p class="abs bio">Lorem ipsum dolor sit amet consectetuer adipiscing sed diam nonummy nibh euismod tincidunt ut laoa aliquam erat volutpat Ut wisi enim ad minim veniam</p>
  <div class="abs socials" aria-label="Social profiles"><span></span><span></span><span></span><span></span><span></span><span></span><span></span></div>
  <div class="abs search"><em>SEARCH</em>
    <svg width="18" height="18" viewBox="0 0 18 18"><circle cx="7.5" cy="7.5" r="5.5" fill="none" stroke="#2c3a48" stroke-width="2"/><line x1="11.5" y1="11.5" x2="16" y2="16" stroke="#2c3a48" stroke-width="2.5"/></svg>
  </div>
  <h3 class="abs side-head" style="top:478px">RECENT POST</h3>
  <div class="abs rpost" style="top:523px">
    <h4>Lorem Ipsum Dolor Sit Amet</h4>
    <p>Lorem ipsum dolor si consectetuer adipiscing sed diam</p>
    <div class="foot"><span>July 8, 2014</span><span class="more">More</span></div>
  </div>
  <div class="abs rdiv"></div>
  <div class="abs rpost" style="top:618px">
    <h4>Lorem Ipsum Dolor Sit Amet</h4>
    <p style="width:220px">Lorem ipsum dolor si consectetuer adipiscing sed diam</p>
    <div class="foot"><span>July 8, 2014</span><span class="more">More</span></div>
  </div>
  <h3 class="abs side-head" style="top:732px">NEWLETTER</h3>
  <div class="abs email"><span>Email</span>
    <svg width="8" height="12" viewBox="0 0 8 12"><path d="M2 2l4 4-4 4" fill="none" stroke="#fff" stroke-width="1.5"/></svg>
  </div>
  <div class="abs cta chirp"><span class="ico"><i></i></span><span class="label">Follow On Chirpline</span></div>
  <div class="abs cta feed"><span class="ico">
    <svg width="20" height="20" viewBox="0 0 20 20"><circle cx="4" cy="16" r="2.5" fill="#fff"/><path d="M2 9a9 9 0 0 1 9 9M2 3a15 15 0 0 1 15 15" fill="none" stroke="#fff" stroke-width="2.6"/></svg>
  </span><span class="label">Subscribe Via RSS</span></div>
  <p class="abs copy">© 2014 Valpirek</p>
</aside>

<main>
  <h2 class="abs post-title">Token-Based PubSub</h2>
  <div class="abs meta">
    <span>By Teskel</span><b>/</b>
    <svg width="15" height="15" viewBox="0 0 15 15"><rect x="1" y="2" width="13" height="12" fill="none" stroke="#333" stroke-width="1.5"/><rect x="1" y="2" width="13" height="3" fill="#333"/><path d="M4 8h2M7 8h2M10 8h2M4 11h2M7 11h2M10 11h2" stroke="#333" stroke-width="1.5"/></svg>
    <span>Jan 23, 2014</span><b>/</b>
    <svg width="18" height="14" viewBox="0 0 18 14"><path d="M0 1h6l2 2h8v3H4L0 13z" fill="#333"/><path d="M4 7h14l-4 7H0z" fill="#333"/></svg>
    <span>Blog</span>
  </div>
  <p class="abs excerpt">Lorem ipsum dolor sit amet, consectetur adipiscing elit. Proin tempus pellentesque consectetur. Morbi tincidunt commodo dui, eu fringilla dui iaculis ac. Vestibulum viverra iaculis dignissim. Ut condimentum, tortor rutrum pellentesque pretium, odio massa varius urna, non dapibus tortor justo eu sem. Vivamus at magna nec justo porta dignissim. Quisque at molestie nulla. Duis at tempus [...]</p>
  <div class="abs share"><span class="lbl">SHARE ON</span><span class="dot"></span><span class="dot"></span><span class="dot"></span><span class="dot"></span></div>
  <div class="abs read">READ MORE</div>
  <h3 class="abs c-head">COMMENTS 15</h3>

  <div class="abs c-ava ava-a" style="left:404px;top:359px" role="img" aria-label="Commenter profile photo"></div>
  <div class="abs c-box" style="left:500px;top:359px;width:648px"><div class="top"><span>Teskel Says:</span><span>February 12, 2014 3:38 pm</span></div><p>Phasellus a felis euismod, convallis leo eget, gravida ligula. Interdum et malesuada fames ac ante ipsum primis in faucibus</p></div>

  <svg class="abs" style="left:406px;top:451px" width="34" height="50" viewBox="0 0 34 50"><path d="M3 2C0 22 10 42 30 44" fill="none" stroke="#333" stroke-width="1.3"/><path d="M24 39l6 5-7 3" fill="none" stroke="#333" stroke-width="1.3"/></svg>
  <div class="abs c-ava ava-b" style="left:449px;top:453px" role="img" aria-label="Commenter profile photo"></div>
  <div class="abs c-box" style="left:544px;top:453px;width:604px"><div class="top"><span>Dapibus Tellus Quis:</span><span>February 12, 2014 3:38 pm</span></div><p>Phasellus a felis euismod, convallis leo eget, gravida ligula. Interdum et malesuada fames ac ante ipsum primis in faucibus</p></div>

  <div class="abs c-ava ava-c" style="left:404px;top:547px" role="img" aria-label="Commenter avatar image of puzzle pieces"></div>
  <div class="abs c-box" style="left:500px;top:547px;width:648px"><div class="top"><span>Teskel Says:</span><span>February 12, 2014 3:38 pm</span></div><p>Phasellus a felis euismod, convallis leo eget, gravida ligula. Interdum et malesuada fames ac ante ipsum primis in faucibus</p></div>

  <div class="abs c-ava ava-d" style="left:404px;top:641px" role="img" aria-label="Commenter avatar image"></div>
  <div class="abs c-box" style="left:500px;top:641px;width:648px"><div class="top"><span>Teskel Says:</span><span>February 12, 2014 3:38 pm</span></div><p>Phasellus a felis euismod, convallis leo eget, gravida ligula. Interdum et malesuada fames ac ante ipsum primis in faucibus</p></div>

  <div class="abs c-ava ava-c" style="left:404px;top:737px" role="img" aria-label="Commenter avatar image of puzzle pieces"></div>
  <div class="abs c-box" style="left:500px;top:737px;width:648px"><div class="top"><span>Teskel Says:</span><span>February 12, 2014 3:38 pm</span></div><p>Phasellus a felis euismod, convallis leo eget, gravida ligula. Interdum et malesuada fames ac ante ipsum primis in faucibus</p></div>

  <div class="abs c-ava ava-a" style="left:404px;top:830px;border-color:transparent;box-shadow:none" role="img" aria-label="Commenter profile photo"></div>
  <div class="abs c-box" style="left:500px;top:830px;width:648px"><div class="top"><span>Teskel Says:</span><span>February 12, 2014 3:38 pm</span></div><p>Phasellus a felis euismod, convallis leo eget, gravida ligula. Interdum et malesuada fames ac ante ipsum primis in faucibus</p></div>

  <div class="abs see-all">SEE ALL</div>
</main>
</body>
</html>
```